New look while maintaining the Brand identification!

I want a new look for my business card. I want to keep the same colors and feel but change the look and layout a bit. The logo (KALMORETIX Physical therapy Reimagined and the lilypad) must remain the same and in that font.
We are a physical therapy clinic. So we have certification that we can write on the back or services we provide (which is what we currently have on the back of the card as well)

Contact information
2840 Cedar Hollow Rd., #22
Naples, FL 34276
P: (239) 555-0172
F: (239) 555-0198
E: kalmoretixcare@mailvexo.com
W: www.kalmoretixcare-example.com

Industry/Entity Type

Physical Therapy

Contact Information for Business Card

Our current cards have the business address and information on the back. But I am willing to have it be in the front.

Font styles to use
Sans Serif

Colors
abd036
fbf289
ec1f27

Requirements
Must have
• Has to be unique!
• Services we provide and/or techniques we do must fit on the card
Nice to have
• Would like to have the front and back somehow linked together. Such that if you set the front next to the back, there is a nice flow of design! Currently the back is white with writing on it.
Should not have
• I like the wave lines as compared to straight lines.

```html
<!DOCTYPE html>
<html lang="en">
<head>
<meta charset="utf-8">
<title>Kalmoretix Business Card</title>
<link href="https://fonts.googleapis.com/css2?family=Open+Sans:wght@400;600;700&display=swap" rel="stylesheet">
<style>
  :root{
    --lime:#a4cc36;
    --lime-deep:#93bd2a;
    --gold:#c9b208;
    --white:#ffffff;
    --ink:#1d1d1b;
    --paper:#f1f1ee;
    --stage:#e6e3dc;
  }
  *{box-sizing:border-box;margin:0;padding:0}
  html,body{width:1200px;height:960px;overflow:hidden}
  body{background:var(--stage);font-family:"Open Sans",Arial,sans-serif;position:relative}
  .card{position:absolute;left:240px;width:720px;height:412px;box-shadow:0 6px 18px rgba(0,0,0,.18)}
  .card--front{top:52px;background:var(--lime);padding:20px}
  .card--back{top:496px;background:var(--white);padding:18px}
  .face{position:relative;width:100%;height:100%;overflow:hidden}
  .texture{position:absolute;inset:0}
  .card--front .texture{background:radial-gradient(ellipse at center,#ffffff 0%,var(--paper) 100%)}
  .card--back .texture{background:radial-gradient(ellipse at center,#acd43f 0%,var(--lime-deep) 100%)}
  .brand{position:absolute;left:0;right:0;display:flex;justify-content:center;align-items:center;gap:12px;font-weight:700;letter-spacing:1px}
  .brand__dot{width:16px;height:16px;border-radius:50%}
  .card--front .brand{top:112px;font-size:54px;color:var(--gold)}
  .card--front .brand__dot{background:var(--gold)}
  .services__title{position:absolute;top:224px;left:0;right:0;text-align:center;color:var(--lime);font-weight:700;font-size:17px;letter-spacing:.5px}
  .rule{position:absolute;left:0;right:0;height:2px}
  .card--front .rule{top:276px;background:var(--lime)}
  .services__list{position:absolute;top:298px;left:0;right:0;display:flex;justify-content:space-around;align-items:center;list-style:none;color:var(--lime);font-weight:600;font-size:19px;padding:0 24px}
  .services__sep{width:7px;height:7px;border-radius:50%;background:var(--lime)}
  .card--back .brand{top:78px;font-size:44px;color:var(--white)}
  .card--back .brand__dot{background:var(--white)}
  .card--back .rule{top:172px;background:var(--white)}
  .contact{position:absolute;top:190px;left:0;right:0;text-align:center;font-size:16px;color:var(--ink);line-height:1.5}
  .contact__address{margin-bottom:6px}
  .contact__row{display:flex;justify-content:center;align-items:center;gap:8px}
  .contact__row--phone{color:var(--white);font-size:21px}
  .contact__row svg{width:14px;height:14px;flex:none}
</style>
</head>
<body>

<section class="card card--front">
  <div class="face">
    <div class="texture" role="img" aria-label="Soft quilted diamond texture on white"></div>
    <div class="brand"><span class="brand__dot"></span><span class="brand__name">KALMORETIX</span></div>
    <h2 class="services__title">OUR SERVICES</h2>
    <div class="rule"></div>
    <ul class="services__list">
      <li>Our Service</li><li class="services__sep"></li>
      <li>Our Service</li><li class="services__sep"></li>
      <li>Our Service</li><li class="services__sep"></li>
      <li>Our Service</li>
    </ul>
  </div>
</section>

<section class="card card--back">
  <div class="face">
    <div class="texture" role="img" aria-label="Soft quilted diamond texture on lime green"></div>
    <div class="brand"><span class="brand__dot"></span><span class="brand__name">KALMORETIX</span></div>
    <div class="rule"></div>
    <address class="contact" style="font-style:normal">
      <p class="contact__address">2840 Cedar Hollow Rd., #22, Naples, FL 34276</p>
      <p class="contact__row contact__row--phone">
        <svg viewBox="0 0 24 24"><path fill="#1d1d1b" d="M6.6 10.8a15 15 0 0 0 6.6 6.6l2.2-2.2a1 1 0 0 1 1-.25 11.4 11.4 0 0 0 3.6.57 1 1 0 0 1 1 1V20a1 1 0 0 1-1 1A17 17 0 0 1 3 4a1 1 0 0 1 1-1h3.5a1 1 0 0 1 1 1c0 1.25.2 2.45.57 3.57a1 1 0 0 1-.25 1z"/></svg>
        (239) 555-0172</p>
      <p class="contact__row contact__row--phone">
        <svg viewBox="0 0 24 24"><rect x="3" y="9" width="18" height="11" rx="2" fill="#1d1d1b"/><rect x="7" y="3" width="10" height="7" fill="#1d1d1b"/></svg>
        (239) 555-0198</p>
      <p class="contact__row" style="margin-top:8px">
        <svg viewBox="0 0 24 24"><rect x="2" y="5" width="20" height="14" rx="1" fill="#ffffff"/><path d="M2 6l10 7 10-7" fill="none" stroke="#93bd2a" stroke-width="2"/></svg>
        kalmoretixcare@mailvexo.com</p>
      <p class="contact__row">
        <svg viewBox="0 0 24 24"><circle cx="12" cy="12" r="9" fill="none" stroke="#ffffff" stroke-width="2"/><path d="M3 12h18M12 3c3 3 3 15 0 18M12 3c-3 3-3 15 0 18" fill="none" stroke="#ffffff" stroke-width="1.5"/></svg>
        www.kalmoretixcare-example.com</p>
    </address>
  </div>
</section>

</body>
</html>
```